Gardener needs an exciting new flyer design.

I'm a passionate gardener that requires a custom flyer design for a owner operator gardening business. Design will be for a DL flyer. I'm based on the Sunshine coast in Queensland Australia. My target audience is the residential market on the Sunshine coast. Business name is Marlowe Greens. My services are, lawn mowing, weeding, Eco Friendly fertilizing, green waste removal, Mulching, tree and shrub pruning, Full garden makeovers, hedging, pressure cleaning, privacy screening, Timber deck rejuvenation, Planting, Turf preparation and installation, and much more. Free no obligation quotes, reliable and friendly service, great rates. 12 years experience. Web www.marlowegreens.com.au - Phone 0418527064 - Email doug@marlowegreens.com.au I would like the design to portray a friendly and professional approach.

Target Market(s)

Residential

Industry/Entity Type

Gardener

Font styles to use
Serif

Colors
9ccb3b
abd037
3176b5

Requirements
Must have
• my services, my logo, my contact details,

```html
<!DOCTYPE html>
<html lang="en">
<head>
<meta charset="utf-8">
<title>Marlowe Greens – DL Flyer</title>
<link rel="stylesheet" href="https://fonts.googleapis.com/css2?family=Bitter:wght@400;700;800&family=Montserrat:wght@600;700&family=Roboto+Condensed:wght@400;700&display=swap">
<style>
  :root {
    --ink: #000000;
    --paper: #e9ece8;
    --white: #ffffff;
    --brand-green: #3f8f2a;
    --name-green: #3e8e35;
    --leaf-green: #6dbb3a;
    --slate: #5f6061;
    --band-grey: #8c8d8f;
    --lawn-light: #7fbf45;
    --lawn-dark: #2f6a22;
  }
  html, body {
    margin: 0;
    width: 1200px;
    height: 2253px;
    overflow: hidden;
    background: var(--paper);
  }
  .flyer {
    position: absolute;
    left: 100px;
    top: 66px;
    width: 1000px;
    height: 2120px;
    display: block;
  }
  .panel-black { fill: var(--ink); }
  .band-grey { fill: var(--band-grey); }
  .divider { fill: #d8d9da; }
  .brand-mark { fill: var(--brand-green); }
  .brand-name {
    font-family: 'Bitter', serif;
    font-weight: 400;
    font-size: 54px;
    fill: var(--name-green);
  }
  .headline {
    font-family: 'Bitter', serif;
    font-weight: 800;
    fill: var(--white);
  }
  .tab { fill: var(--brand-green); }
  .tab-title {
    font-family: 'Bitter', serif;
    font-weight: 700;
    font-size: 28px;
    fill: var(--white);
  }
  .service {
    font-family: 'Montserrat', sans-serif;
    font-weight: 600;
    font-size: 20px;
    fill: var(--white);
  }
  .bullet { fill: none; stroke: var(--leaf-green); stroke-width: 1.8; }
  .benefits-panel { fill: var(--slate); }
  .benefits-title {
    font-family: 'Bitter', serif;
    font-weight: 700;
    font-size: 28px;
    fill: var(--white);
  }
  .benefit {
    font-family: 'Montserrat', sans-serif;
    font-weight: 700;
    font-size: 18px;
    fill: var(--white);
  }
  .cta-panel { fill: var(--brand-green); }
  .experience {
    font-family: 'Bitter', serif;
    font-weight: 700;
    font-size: 27px;
    fill: var(--white);
  }
  .call {
    font-family: 'Roboto Condensed', sans-serif;
    font-weight: 700;
    font-size: 46px;
    fill: var(--white);
  }
  .phone {
    font-family: 'Roboto Condensed', sans-serif;
    font-weight: 400;
    font-size: 19px;
    fill: var(--white);
  }
  .footer-rule { fill: var(--brand-green); }
  .footer-text {
    font-family: 'Roboto Condensed', sans-serif;
    font-weight: 400;
    font-size: 19px;
    fill: var(--white);
  }
  .icon-fill { fill: var(--leaf-green); }
  .icon-white { fill: var(--white); }
</style>
</head>
<body>
<svg class="flyer" viewBox="0 0 609 1291" xmlns="http://www.w3.org/2000/svg">
  <defs>
    <linearGradient id="lawn" x1="0" y1="0" x2="0" y2="1">
      <stop offset="0" stop-color="#6f8a5a"/>
      <stop offset="0.35" stop-color="#4f7a36"/>
      <stop offset="0.7" stop-color="var(--lawn-light)"/>
      <stop offset="1" stop-color="var(--lawn-dark)"/>
    </linearGradient>
  </defs>

  <!-- header -->
  <rect class="panel-black" x="0" y="0" width="609" height="1291"/>
  <g class="brand">
    <circle class="brand-mark" cx="304" cy="150" r="62"/>
    <text class="brand-name" x="304" y="300" text-anchor="middle">Marlowe Greens</text>
  </g>

  <!-- hero -->
  <rect class="band-grey" x="0" y="350" width="609" height="18"/>
  <polygon role="img" aria-label="Photo of a suburban house with a lush green lawn and colourful flower beds" fill="url(#lawn)" points="0,368 609,368 609,812 0,765"/>
  <polygon class="divider" points="0,761 609,806 609,816 0,770"/>
  <text class="headline" x="34" y="690" font-size="43">A BEAUTIFUL GARDEN</text>
  <text class="headline" x="34" y="738" font-size="35">DOESN’T HAPPEN BY ITSELF</text>

  <!-- services -->
  <polygon class="tab" points="0,812 258,812 240,852 0,852"/>
  <text class="tab-title" x="34" y="842">Our Services</text>

  <g class="services">
    <g class="bullets">
      <path class="bullet" d="M42,884 q1,-12 8,-14 q0,10 -8,14z"/>
      <path class="bullet" d="M42,912 q1,-12 8,-14 q0,10 -8,14z"/>
      <path class="bullet" d="M42,940 q1,-12 8,-14 q0,10 -8,14z"/>
      <path class="bullet" d="M42,968 q1,-12 8,-14 q0,10 -8,14z"/>
      <path class="bullet" d="M42,996 q1,-12 8,-14 q0,10 -8,14z"/>
      <path class="bullet" d="M42,1025 q1,-12 8,-14 q0,10 -8,14z"/>
      <path class="bullet" d="M42,1053 q1,-12 8,-14 q0,10 -8,14z"/>
      <path class="bullet" d="M42,1081 q1,-12 8,-14 q0,10 -8,14z"/>
      <path class="bullet" d="M42,1109 q1,-12 8,-14 q0,10 -8,14z"/>
      <path class="bullet" d="M42,1138 q1,-12 8,-14 q0,10 -8,14z"/>
      <path class="bullet" d="M42,1166 q1,-12 8,-14 q0,10 -8,14z"/>
      <path class="bullet" d="M42,1194 q1,-12 8,-14 q0,10 -8,14z"/>
      <path class="bullet" d="M42,1222 q1,-12 8,-14 q0,10 -8,14z"/>
    </g>
    <text class="service" x="56" y="884">Lawn Mowing</text>
    <text class="service" x="56" y="912">Weeding</text>
    <text class="service" x="56" y="940">Eco Friendly Fertilizing</text>
    <text class="service" x="56" y="968">Green Waste Removal</text>
    <text class="service" x="56" y="996">Mulching</text>
    <text class="service" x="56" y="1025">Tree and Shrub Pruning</text>
    <text class="service" x="56" y="1053">Full Garden Makeovers</text>
    <text class="service" x="56" y="1081">Hedging</text>
    <text class="service" x="56" y="1109">Pressure Cleaning</text>
    <text class="service" x="56" y="1138">Privacy screening</text>
    <text class="service" x="56" y="1166">Timber Deck Rejuvenation</text>
    <text class="service" x="56" y="1194">Planting</text>
    <text class="service" x="56" y="1222">Turf Preparation and Installation</text>
  </g>

  <!-- benefits -->
  <polygon class="benefits-panel" points="278,806 609,822 609,1060 366,1060"/>
  <text class="benefits-title" x="469" y="870" text-anchor="middle">BENEFITS</text>
  <g class="benefits" text-anchor="middle">
    <text class="benefit" x="469" y="912">Free no</text>
    <text class="benefit" x="469" y="935">obligation quotes</text>
    <text class="benefit" x="469" y="968">Reliable and</text>
    <text class="benefit" x="469" y="991">Friendly Service</text>
    <text class="benefit" x="469" y="1027">Great Rates</text>
  </g>

  <!-- call to action -->
  <path class="cta-panel" d="M398,1056 L609,1056 L609,1241 L436,1241 L384,1072 Q381,1056 398,1056 Z"/>
  <text class="experience" x="513" y="1094" text-anchor="middle">12 Years</text>
  <text class="experience" x="513" y="1126" text-anchor="middle">Experience</text>
  <text class="call" x="513" y="1183" text-anchor="middle">Call US</text>
  <path class="icon-white" d="M451,1199 q-3,2 -1,7 q3,6 8,7 q3,1 5,-2 l-3,-3 l-2,2 q-3,-1 -5,-5 l2,-2 z"/>
  <text class="phone" x="468" y="1213">0418527064</text>

  <!-- footer -->
  <rect class="footer-rule" x="0" y="1240" width="609" height="4"/>
  <g class="footer">
    <rect class="icon-fill" x="36" y="1262" width="13" height="9" rx="1"/>
    <text class="footer-text" x="56" y="1273">doug@marlowegreens.com.au</text>
    <circle class="icon-fill" cx="314" cy="1266" r="6"/>
    <text class="footer-text" x="326" y="1273">www.marlowegreens.com.au</text>
  </g>
</svg>
</body>
</html>
```